依頼詳細
6月2日は感謝を伝えるペルミナの日であることが日本の当たり前の記念日になることが最終目的です。
そのためのイベント企画として、
「ありがとう」を伝えたい人、もの、コトを広く募集するためのチラシのデザインをお願いします。
主催は、一般社団法人ミルデン香木文化協会とTovelWorksです。
宣伝は、WEBと紙の両方で行います。
毎年、6月2日に発表し、受賞者に賞状をお送りする予定です。

記載項目
6月2日は感謝を伝えるペルミナの日
6月2日はペルミナの日
6月2日はありがとうを伝えるペルミナの日
日頃の感謝の思いを伝えたい人、もの、コト
ペルミナの日に発表
2020年から毎年開催!その第1回

ペルミナの日とは?
https://www.tovelworks-example.com/6-2

一般社団法人ミルデンンローズ文化協会http://www.milden-koboku-example.or.jp/

トーベルワークス
https://www.tovelworks-example.com/

サイズ
A4
ページ数
片面
希望イメージ
シンプル 複雑
単色 カラフル
暗い 明るい
日常 高級
遊び心 厳粛
未来的 伝統的
女性的 男性的
希望する色
赤系、薔薇のイメージ
納品ファイル
• 高解像度JPG (.jpg)
• イラストレーター形式 (.ai)
• フォトショップ形式 (.psd)
• PNG形式 (.png)
補足説明
お世話になっております。
まもなく締め切りですが、たまたま本日急用ができ、このタイミングでの確認が難しい状況です。
そのままで決定的なものがないので、
若干の修正をセットで、期間修了後に決定させていただいてもよろしいでしょうか。
■ 選んだ理由

募集目的が明確に表現されていたことと、6月2日はペルミナの日であることが、この1枚でインプットされるような気がしたこと。
全体のまとまり、上品さがなども含め決め手となりましたのと、こちらの要望への対応が早かったことがとてもうれしく感じられました。

■ 提案者全員のお礼・コメント

素敵なご提案をたくさんありがとうございました。
どれもとても素晴らしく、特にいくつか最後まで迷いました。
こちらの不慣れさと不手際でご迷惑をおかけした方もいらしたと思います。
申し訳ございませんでした。
今後もお願いすることがあると思います。
どうぞよろしくお願い申し上げます。
本当にありがとうございました。

```html
<!DOCTYPE html>
<html lang="ja">
<head>
<meta charset="UTF-8">
<title>6月2日は感謝を伝えるペルミナの日</title>
<link rel="stylesheet" href="https://fonts.googleapis.com/css2?family=Bodoni+Moda:wght@500;700&family=Josefin+Sans:wght@300;400&family=Noto+Sans+JP:wght@300;400&display=swap">
<style>
  :root {
    --rose: #d9336f;
    --rose-deep: #8c1d3e;
    --rose-soft: #ee8db0;
    --blush: #fbe6ee;
    --ink: #1a1a1a;
    --white: #ffffff;
  }
  * { margin: 0; padding: 0; box-sizing: border-box; }
  html, body { width: 846px; height: 1200px; overflow: hidden; background: var(--white); }
  .flyer { position: relative; width: 846px; height: 1200px; background: var(--rose); overflow: hidden; font-family: "Noto Sans JP", sans-serif; }
  .rose-pattern {
    position: absolute; left: 0; top: 0; width: 846px; height: 470px;
    background: linear-gradient(180deg, var(--white) 0%, var(--blush) 60%, #f8d3e0 100%);
  }
  .date { position: absolute; left: 0; top: 32px; width: 846px; text-align: center; color: var(--ink); }
  .date__day-small { font-family: "Bodoni Moda", serif; font-weight: 700; font-size: 30px; line-height: 1; }
  .date__month { font-family: "Josefin Sans", sans-serif; font-weight: 400; font-size: 22px; letter-spacing: 3px; margin-top: 4px; }
  .date__day-large { font-family: "Bodoni Moda", serif; font-weight: 500; font-size: 330px; line-height: 1; margin-top: -10px; }
  .bands { position: absolute; left: 0; top: 360px; width: 846px; height: 170px; }
  .headline { position: absolute; left: 0; top: 510px; width: 846px; text-align: center; color: var(--white); }
  .headline__title { font-family: "Josefin Sans", sans-serif; font-weight: 300; font-size: 34px; letter-spacing: 2px; }
  .headline__sub { font-weight: 300; font-size: 19px; letter-spacing: 2px; margin-top: 4px; }
  .lead { position: absolute; left: 0; top: 612px; width: 846px; text-align: center; color: var(--white); font-size: 19px; line-height: 1.75; letter-spacing: 1px; }
  .body { position: absolute; left: 96px; top: 712px; width: 654px; color: var(--white); font-size: 13px; line-height: 1.85; font-weight: 300; }
  .body p + p { margin-top: 20px; }
  .organizer { position: absolute; left: 0; top: 1132px; width: 846px; text-align: center; color: var(--white); font-size: 12px; letter-spacing: 1px; }
</style>
</head>
<body>
<main class="flyer">
  <div class="rose-pattern" role="img" aria-label="白地に描かれたピンクの線画の薔薇の模様"></div>

  <div class="date">
    <div class="date__day-small">6</div>
    <div class="date__month">JUNE</div>
    <div class="date__day-large">2</div>
  </div>

  <svg class="bands" viewBox="0 0 846 170" preserveAspectRatio="none" aria-hidden="true">
    <path d="M0 60 C 200 40, 380 80, 560 40 C 680 15, 780 20, 846 30 L846 170 L0 170 Z" fill="var(--rose-soft)"/>
    <path d="M0 20 C 180 40, 380 100, 520 120 C 620 130, 700 110, 846 90 L846 170 L0 170 Z" fill="var(--rose-deep)"/>
    <path d="M0 100 C 200 110, 400 150, 560 140 C 680 130, 780 110, 846 100 L846 170 L0 170 Z" fill="var(--rose)"/>
  </svg>

  <header class="headline">
    <h1 class="headline__title">HAPPY PERMINA DAY</h1>
    <p class="headline__sub">6月2日は感謝を伝えるペルミナの日</p>
  </header>

  <p class="lead">ペルミナの日にちなんで「ありがとう」を伝えたい人、<br>もの、コトを広く募集いたします。</p>

  <section class="body">
    <p>香木の国ミルデンで行われている、香木を通して感謝を伝える文化を日本でも広めるために、2011年に駐日ミルデン大使によって6月2日は「ありがとう」の気持ちを伝えあう愛と感謝の記念日「ペルミナの日」となりました。</p>
    <p>そんなペルミナの日をもっと広めていくために、今回皆さんの「ありがとう」を伝えたい人、もの、コトを募集いたします。応募の中から選ばれた方は6月2日のペルミナの日に掲載し、賞状をお送りいたします。<br>この機会に、日ごろの感謝を大切な人、もの、コトに伝えてみませんか？</p>
    <p>ぜひ皆さんのご応募をお待ちしております。</p>
  </section>

  <footer class="organizer">主催　一般社団法人ミルデン香木文化協会＆トーベルワークス</footer>
</main>
</body>
</html>
```